Business Card Design for a Lending Business (Hard Money loans)

We need a business card for our Real Estate Lending business. We do hard Money loans for real estate investors. We have an existing logo we like, see attached. I'd like the business card to mostly include the logo colors, but a bright color pop of some sort would be nice to see also. Card should include Logo, Company Name, Company Address, Employee Name, Cell Phone, Main Phone, Email, Website

Industry/Entity Type

Finance / Lending

Contact Information for Business Card

Logo, Company Name, Company Address, Employee Name, Cell Phone, Main Phone, Email, Website

Requirements
Nice to have
• I'd like the business card to mostly include the logo colors, but a bright color pop of some sort would be nice to see also.

```html
<!DOCTYPE html>
<html lang="en">
<head>
<meta charset="utf-8">
<title>Crestline Lending – Business Card</title>
<link rel="stylesheet" href="https://fonts.googleapis.com/css2?family=Montserrat:wght@700;800&family=Open+Sans:wght@400;600&display=swap">
<style>
  :root {
    --backdrop: #4a4a4a;
    --card: #151515;
    --navy: #2b3686;
    --cyan: #00aee0;
    --white: #f2f2f2;
  }
  * { box-sizing: border-box; margin: 0; padding: 0; }
  html, body { width: 1200px; height: 801px; overflow: hidden; }
  body {
    background: var(--backdrop);
    font-family: "Open Sans", Arial, sans-serif;
    color: var(--white);
    position: relative;
  }
  .card {
    position: absolute;
    top: 245px;
    width: 540px;
    height: 310px;
    background: var(--card);
    border-radius: 18px;
    border-bottom: 4px solid var(--cyan);
    box-shadow: 0 14px 30px rgba(0,0,0,0.45);
    overflow: hidden;
  }
  .card--front { left: 45px; }
  .card--back { left: 615px; }

  /* brand wordmark */
  .brand {
    position: absolute;
    display: flex;
    align-items: center;
    font-family: "Montserrat", Arial, sans-serif;
    font-weight: 800;
    color: var(--navy);
    text-transform: uppercase;
    line-height: 1.05;
  }
  .brand__dot {
    flex: none;
    border-radius: 50%;
    background: var(--navy);
  }
  .card--front .brand { left: 30px; top: 120px; gap: 12px; font-size: 24px; letter-spacing: 3px; }
  .card--front .brand__dot { width: 34px; height: 34px; }
  .card--back .brand { left: 0; right: 0; top: 0; bottom: 0; justify-content: center; gap: 20px; font-size: 40px; letter-spacing: 6px; }
  .card--back .brand__dot { width: 56px; height: 56px; }

  /* person */
  .person {
    position: absolute;
    right: 30px;
    top: 36px;
    text-align: right;
  }
  .person__name {
    font-family: "Montserrat", Arial, sans-serif;
    font-weight: 800;
    font-size: 22px;
    letter-spacing: 0.3px;
  }
  .person__first { color: var(--navy); }
  .person__last { color: var(--cyan); }
  .person__title { font-size: 12px; margin-top: 2px; }

  .divider {
    position: absolute;
    left: 190px;
    right: 118px;
    top: 94px;
    height: 1.5px;
    background: var(--cyan);
  }

  .address {
    position: absolute;
    right: 30px;
    top: 150px;
    text-align: right;
    font-size: 12.5px;
    line-height: 1.45;
  }

  .contacts {
    position: absolute;
    left: 205px;
    bottom: 34px;
    list-style: none;
    font-size: 13px;
    line-height: 1.55;
  }
  .contacts li { display: flex; align-items: center; gap: 8px; }
  .contacts svg { width: 12px; height: 12px; flex: none; }
</style>
</head>
<body>

  <section class="card card--front" aria-label="Card front">
    <div class="brand">
      <span class="brand__dot"></span>
      <span class="brand__name">Crestline<br>Lending</span>
    </div>

    <div class="person">
      <div class="person__name"><span class="person__first">Dana</span> <span class="person__last">Whitfield</span></div>
      <div class="person__title">Managing Director</div>
    </div>

    <div class="divider"></div>

    <div class="address">Your address, City<br>State, Zip 1234</div>

    <ul class="contacts">
      <li>
        <svg viewBox="0 0 12 12" aria-hidden="true"><rect x="3" y="0.8" width="6" height="10.4" rx="1" fill="none" stroke="#00aee0" stroke-width="1.2"/><circle cx="6" cy="9.3" r="0.7" fill="#00aee0"/></svg>
        123 456 789
      </li>
      <li>
        <svg viewBox="0 0 12 12" aria-hidden="true"><path d="M2.5 1 L4.5 1 L5.3 3.6 L4 4.6 C4.7 6.2 5.8 7.3 7.4 8 L8.4 6.7 L11 7.5 L11 9.5 C11 10.4 10.3 11 9.5 11 C5.3 10.7 1.3 6.7 1 2.5 C1 1.7 1.6 1 2.5 1 Z" fill="#00aee0"/></svg>
        123 456 789
      </li>
      <li>
        <svg viewBox="0 0 12 12" aria-hidden="true"><rect x="0.8" y="2.2" width="10.4" height="7.6" rx="0.8" fill="#00aee0"/><path d="M1 2.6 L6 6.6 L11 2.6" fill="none" stroke="#151515" stroke-width="1"/></svg>
        info@yourmail.com
      </li>
      <li>
        <svg viewBox="0 0 12 12" aria-hidden="true"><circle cx="6" cy="6" r="5" fill="none" stroke="#00aee0" stroke-width="1.2"/><ellipse cx="6" cy="6" rx="2.2" ry="5" fill="none" stroke="#00aee0" stroke-width="1"/><line x1="1" y1="6" x2="11" y2="6" stroke="#00aee0" stroke-width="1"/></svg>
        www.yourwebsite.com
      </li>
    </ul>
  </section>

  <section class="card card--back" aria-label="Card back">
    <div class="brand">
      <span class="brand__dot"></span>
      <span class="brand__name">Crestline<br>Lending</span>
    </div>
  </section>

</body>
</html>
```